Wellness Center brochure

I need a brochure designed that will give prospective clients and prospective referring providers (such as doctors) an initial understanding of our practice which is a wellness center that includes progressive Physical Therapy, manual therapy (like massage but more comprehensive and holistic), nutritional wellness, natural lifestyle coaching, and community education in healthy living. In the brochure, I would love to have our logo displayed as well as ample room for copy and possibly some photos (or not).

Wellness

```html
<!DOCTYPE html>
<html lang="en">
<head>
<meta charset="utf-8">
<title>Harmony Roots Physical Therapy – Brochure</title>
<link rel="stylesheet" href="https://fonts.googleapis.com/css2?family=Lato:wght@400;700&display=swap">
<style>
  :root {
    --purple: #7a2a82;
    --purple-deep: #56205f;
    --purple-soft: #a65aab;
    --lilac: #c99ad0;
    --green: #8cc63f;
    --green-mid: #5f9e35;
    --green-dark: #2f7a2f;
    --label: #7a2a82;
    --white: #ffffff;
  }
  * { margin: 0; padding: 0; box-sizing: border-box; }
  html, body { width: 1200px; height: 933px; overflow: hidden; background: var(--white); }
  .brochure {
    position: relative;
    width: 1200px;
    height: 933px;
    font-family: "Lato", sans-serif;
    color: var(--white);
    overflow: hidden;
  }
  .wave { position: absolute; inset: 0; }
  .photo-label {
    position: absolute;
    top: 108px;
    font-weight: 700;
    font-size: 17px;
    color: var(--label);
  }
  .photo-label--left { left: 124px; }
  .photo-label--middle { left: 563px; }

  .brand-name {
    font-family: "Lato", sans-serif;
    font-weight: 700;
    color: var(--green-dark);
    white-space: nowrap;
    display: flex;
    align-items: center;
    gap: 8px;
  }
  .brand-dot {
    width: 24px; height: 24px; border-radius: 50%;
    background: var(--green);
    flex: none;
  }
  .brand-name--header {
    position: absolute;
    top: 112px;
    right: 50px;
    font-size: 21px;
  }

  .accent-area {
    position: absolute;
    left: 1050px; top: 178px;
    width: 120px; height: 92px;
    background: radial-gradient(ellipse at 50% 50%, var(--green-mid) 0%, rgba(95,158,53,0.55) 45%, rgba(95,158,53,0) 72%);
  }

  .services {
    position: absolute;
    left: 830px; top: 317px;
    list-style: none;
    font-weight: 700;
    font-size: 17px;
  }
  .services li { position: relative; padding-left: 26px; height: 45px; }
  .services li::before { content: "•"; position: absolute; left: 0; }

  .about {
    position: absolute;
    left: 77px; top: 450px;
    width: 300px;
    font-size: 17px;
    line-height: 33px;
  }
  .about p + p { margin-top: 33px; }

  .motif-area {
    position: absolute;
    left: 800px; top: 530px;
    width: 390px; height: 403px;
    border-radius: 50% 50% 0 0;
    background: radial-gradient(ellipse at 50% 60%, var(--lilac) 0%, var(--purple-soft) 45%, var(--purple) 80%);
    opacity: 0.7;
  }

  .contact {
    position: absolute;
    left: 423px; top: 716px;
    width: 350px; height: 217px;
    background: var(--purple-deep);
    text-align: center;
    font-weight: 700;
    font-size: 17px;
    padding-top: 36px;
  }
  .contact li { list-style: none; height: 45px; }
  .brand-pill {
    position: absolute;
    left: 418px; top: 690px;
    width: 362px; height: 50px;
    background: var(--white);
    border-radius: 25px;
    display: flex; align-items: center; justify-content: center;
  }
  .brand-name--pill { font-size: 19px; }
</style>
</head>
<body>
<main class="brochure">
  <svg class="wave" width="1200" height="933" viewBox="0 0 1200 933" aria-hidden="true">
    <path d="M0,452 C190,335 420,255 640,256 C830,258 1000,285 1200,168 L1200,933 L0,933 Z" fill="var(--purple)"/>
    <path d="M0,452 C190,335 420,255 640,256 C830,258 1000,285 1200,168" fill="none" stroke="var(--green)" stroke-width="6"/>
  </svg>

  <span class="photo-label photo-label--left">photo</span>
  <span class="photo-label photo-label--middle">photo</span>

  <div class="brand-name brand-name--header"><span class="brand-dot"></span>Harmony Roots Physical Therapy</div>

  <div class="accent-area" role="img" aria-label="Green decorative accent"></div>

  <ul class="services">
    <li>progressive physical therapy</li>
    <li>manual therapy nutritional wellness</li>
    <li>natural lifestyle coaching</li>
    <li>community education in healthy</li>
  </ul>

  <section class="about">
    <p>Text information about Harmony Roots Physical Therapy here. Text information about Harmony Roots Physical Therapy here. Text information about Harmony Roots Physical Therapy here. Text information about Harmony Roots Physical Therapy here. Text information about Harmony Roots Physical Therapy here.</p>
    <p>Text information about Harmony Roots Physical Therapy here.</p>
  </section>

  <div class="motif-area" role="img" aria-label="Large faint decorative background motif"></div>

  <section class="contact">
    <ul>
      <li>Address • Address • Address</li>
      <li>Phone</li>
      <li>Email</li>
      <li>Website</li>
    </ul>
  </section>
  <div class="brand-pill">
    <div class="brand-name brand-name--pill">Harmony Roots Physical Therapy</div>
  </div>
</main>
</body>
</html>
```